Business Card Design.

Life and Wellness Coach
www.brightpathwell.net
Want to use my name as the logo it could be the initials TRK or my full name. I want to trade mark me.
I like clean lines and simple designs, but it pops using the colors scheme (one or two colors) on the website.
I provide life and health coaching virtually and in person. My services include: Dietary Signal Screening, Sensitivity Clearing Review, Wellness Coaching, Life Coaching. Life and Health Assessments, and I sell foundational health products and specialized nutrition. Use colors that represent healing and trust.
Target Market(s)
Women for the ages of 30 - 60
Industry/Entity Type
Health
Contact Information for Business Card
Tessa Rosalind Kimble
Life and Wellness Coach
tessa@coachtrk.net
www.brightpathwell.net
555-217-8364
Health is not an event it's a lifestyle (tag line or if you have a better tag line)

```html
<!DOCTYPE html>
<html lang="en">
<head>
<meta charset="utf-8">
<title>Tessa Rosalind Kimble — Business Card</title>
<link href="https://fonts.googleapis.com/css2?family=Ubuntu:wght@400;500;700&display=swap" rel="stylesheet">
<style>
  :root {
    --stage: #e9eaee;
    --card-white: #ffffff;
    --brand-blue: #353f7c;
    --tagline-navy: #2e3a78;
    --text-light: #ffffff;
    --portrait-top: #f3ece8;
    --portrait-hair: #5a3427;
    --portrait-dress: #2f3e8f;
  }
  * { box-sizing: border-box; margin: 0; padding: 0; }
  html, body {
    width: 1200px; height: 1000px; overflow: hidden;
    background: var(--stage);
    font-family: "Ubuntu", "Helvetica Neue", Arial, sans-serif;
  }
  .card {
    position: absolute; left: 100px; top: 214px;
    width: 1000px; height: 572px;
    background: var(--card-white);
    box-shadow: 0 10px 30px rgba(0,0,0,0.18);
    overflow: hidden;
  }
  .portrait {
    position: absolute; left: 0; top: 0;
    width: 430px; height: 572px;
    background: linear-gradient(160deg, var(--portrait-top) 0%, #e7c9b8 35%, var(--portrait-hair) 60%, var(--portrait-dress) 100%);
  }
  .contact-panel {
    position: absolute; left: 430px; top: 0;
    width: 570px; height: 440px;
    background: var(--brand-blue);
    color: var(--text-light);
  }
  .name-row {
    position: absolute; left: 0; right: 0; top: 64px;
    display: flex; align-items: center;
  }
  .name-rule { height: 2px; background: var(--text-light); }
  .name-rule--left { width: 80px; margin-right: 14px; }
  .name-rule--right { flex: 1; margin-left: 14px; }
  .name {
    font-weight: 700; font-size: 27px; letter-spacing: 0.3px; white-space: nowrap;
  }
  .role {
    position: absolute; right: 88px; top: 100px;
    font-size: 19px; font-weight: 400;
  }
  .contact-list {
    position: absolute; right: 48px; top: 206px;
    list-style: none; text-align: right;
    font-size: 24px; font-weight: 500; line-height: 1.4;
  }
  .tagline-band {
    position: absolute; left: 430px; top: 440px;
    width: 570px; height: 132px;
    display: flex; align-items: center; justify-content: flex-end;
    padding-right: 44px;
  }
  .tagline {
    color: var(--tagline-navy); font-size: 27px; font-weight: 500;
  }
</style>
</head>
<body>
  <div class="card">
    <div class="portrait" role="img" aria-label="Portrait photograph of the coach, smiling, in a blue top with a necklace"></div>

    <section class="contact-panel">
      <div class="name-row">
        <span class="name-rule name-rule--left"></span>
        <h1 class="name">Tessa Rosalind Kimble</h1>
        <span class="name-rule name-rule--right"></span>
      </div>
      <p class="role">Life and Wellness Coach</p>
      <ul class="contact-list">
        <li>Phone : 555-217-8364</li>
        <li>Email : tessa@coachtrk.net</li>
        <li>Website : www.brightpathwell.net</li>
      </ul>
    </section>

    <footer class="tagline-band">
      <p class="tagline">Health is not an event it's a lifestyle</p>
    </footer>
  </div>
</body>
</html>
```